Harrowby Wine Label - Design a front and smaller back label for an exclusive red wine

Harrowby Wines produces a very high quality, high priced wine from an old and prestigous vineyard in one of Australia's oldest, but smallest wine growing regions. The grapevines are old (like old men with gnarled arms and trunks) and they produce fewer grapes than younger vines but the grape quality (and thus wine quality) is magnificent and highly sought after as it produces wine of exceptional quality.
The vineyard was purchased by the Harrowby family in February 2010 from a multinational wine company who made wonderful, trophy winning wines for 10 years before the vineyard went into a decline.
The challenge is to produce 2 labels - a simple main front label that focuses on the Harrowby brand and a smaller, information rich, back label that relates the history of the vineyard.
The labels should have a white or charcoal grey background and impart tradition, quality, exclusivity and a little self indulgence which is why we want the family crest incorporated - the choice of font will help.
It might also impart a sense of fun so that it appeals to the 25-35 year old age bracket.
The label should be kept clean and simple not loud and busy. Preferred colours are black, grey and white. Red is fine if used sparingly

Here are the details:_

Front Label (115 long x 65-90mm wide)

Harrowby
Lanternwatch Reserve
2011
Mudgee
Wine of Australia 750ml

Back Label (dimensions to suit text and front label design; font size small; text in black so that it is readable in less than optimal light (eg candlelight at a restaurant table).

Harrowby
Lanternwatch Reserve 2011

This is the first release of The Lanternwatch’s Reserve – just 100 dozen bottles were made. The wine was made from Shiraz and 10% Cabernet Sauvignon grapes sourced from an iconic Mudgee vineyard that was established 1966 by Peter Vallis. In 1994, the vineyard known as ”Silver Hollow”, became the source of a decade of formidable, trophy winning wines under Tindalberg’s and later Quellwood’s ownership. The 20ha vineyard was purchased by Corin & Margaret Harrowby in 2010. The Silver Hollow name was retained by Quellwoods; no wine has been released under this label since the 2006 vintage.

The shaky old Shiraz vines are slowly being restored to full health using careful cane pruning techniques that stimulates fresh, new tissue growth, more even bunch sizes and better grape quality and consistency. The Shiraz grapes used in this wine were hand-picked from two rows of the first crop from the 46 year old, cane pruned vines. The 2011 Reserve is the first step to re-establish the traditions of a famous vineyard and one of Australia’s most sought after export wines.

“Deep and intense purple hues with aromas of ripe blackberry fruits, spice and eucalypt with rich chocolate complemented by subtle oak overtones. A rich and full bodied wine exhibiting a soft yet generous palate with plum, forest fruits and mint chocolate notes. A fine grained tannin structure displaying integrated oak characters adds to the complexity of the wine. This wine was aged for 18 months in a blend of new French oak hogsheads and one year old American hogsheads, crafting a blend with great structure and length of flavour which will develop into a Mudgee classic” – Lewis Farrant, Winemaker

13.5% Alc/Vol.
Contains approx 8.0 std drinks
Preservative (220) added

Harrowby Wines
Tallowbend Rd, Mudgee 2850
www.harrowbywines.example.au

Reason: My apologies to the designers who have kindly submitted some wonderful designs. I am trying to achieve a conscentious between shareholders. This is difficult as they are in different parts of the world and I have learned through this experience that opinions on wine labels are quite diverse!!! The feedback I have received so far indicates the following (1) A light or white background is preferred (2) The crest should not be a dominant part of the label (3) The label needs to be clean, fresh and uncomplicated (4) If red is used it should be in minor detail only (5) "Harrowby" should be distinctive. The font is difficult for us! (6) We are considering "The Lanternwatch" RESERVE instead of "Lanternwatch's" RESERVE (7) The text on the back label is too long; I will edit and re-upload Many thanks for your help and patience Kind regards Corin

Good Morning All,
I have edited the back label text to reduce the size of the label. A Word file with the changes has just been uploaded.
Cheers
Corin

Dear Designers,
Thank you all so very much for the wonderful selection of designs you have submitted my family have all been overwhelmed by the quality and skill level exhibited and we all appreciate you your efforts
Kindest regards
Corin

Target Market(s)

25-35 year old men and women of Australia, China, US & UK

Industry/Entity Type

Restaurant

Requirements
Must have
• Crest
Should not have
• Animals on the label

```html
<!DOCTYPE html>
<html lang="en">
<head>
<meta charset="utf-8">
<title>Harrowby Wines – Lanternwatch's Reserve Labels</title>
<link rel="stylesheet" href="https://fonts.googleapis.com/css2?family=Arimo:wght@400&family=Crimson+Text:wght@400&family=Raleway:wght@400&family=Oswald:wght@600&display=swap">
<style>
  :root {
    --paper: #ffffff;
    --ink: #1a1a1a;
    --charcoal: #231f20;
    --slate: #6d6e70;
    --title-grey: #5a5a5a;
    --wine-red: #b3252b;
    --key-dark: #4a4a4a;
    --key-light: #a6a6a6;
    --rule: #333333;
  }
  * { margin: 0; padding: 0; box-sizing: border-box; }
  html, body { width: 1200px; height: 896px; overflow: hidden; background: var(--paper); }
  body { position: relative; font-family: "Crimson Text", serif; color: var(--ink); }

  .caption {
    position: absolute;
    font-family: "Arimo", sans-serif;
    font-size: 13px;
    color: var(--ink);
    text-align: center;
  }
  .caption--front-title { left: 451px; top: 209px; width: 257px; font-size: 14px; }
  .caption--back-title { left: 809px; top: 209px; width: 327px; font-size: 14px; }
  .caption--front-size { left: 451px; top: 694px; width: 257px; font-size: 11px; }
  .caption--back-size { left: 809px; top: 694px; width: 327px; font-size: 11px; }

  /* Front label */
  .front-label {
    position: absolute;
    left: 451px; top: 250px;
    width: 258px; height: 421px;
    border: 1px solid var(--rule);
    border-radius: 2px;
    background: var(--paper);
    overflow: hidden;
  }
  .front-label__title {
    position: absolute; top: 44px; left: 0; width: 100%;
    text-align: center;
    font-family: "Raleway", sans-serif;
    font-size: 12.5px;
    letter-spacing: 3.2px;
    line-height: 16px;
    color: var(--title-grey);
  }
  .front-label__keys {
    position: absolute; left: 88px; top: 95px;
    width: 80px; height: 95px;
    background: radial-gradient(ellipse at 50% 35%, var(--key-light), var(--key-dark) 75%, transparent 76%);
  }
  .front-label__vintage {
    position: absolute; top: 200px; width: 100%;
    text-align: center;
    font-family: "Raleway", sans-serif;
    font-size: 12px; letter-spacing: 2px;
    color: var(--title-grey);
  }
  .front-label__red-rule {
    position: absolute; left: 0; top: 277px; width: 100%; height: 6px;
    background: var(--wine-red);
  }
  .front-label__band {
    position: absolute; left: 0; top: 283px; width: 100%; height: 100px;
    background: var(--charcoal);
  }
  .front-label__crest-mark {
    position: absolute; left: 116px; top: 248px;
    width: 26px; height: 26px;
    background: var(--paper);
    border: 2px solid var(--charcoal);
  }
  .brand-name {
    font-family: "Crimson Text", serif;
    font-weight: 400;
    color: var(--paper);
    white-space: nowrap;
  }
  .front-label__brand {
    position: absolute; top: 318px; width: 100%;
    text-align: center;
    font-size: 30px;
  }
  .front-label__region {
    position: absolute; top: 397px; width: 100%;
    text-align: center;
    font-family: "Raleway", sans-serif;
    font-size: 7.5px; letter-spacing: 1.2px;
    color: var(--ink);
  }

  /* Back label */
  .back-label {
    position: absolute;
    left: 809px; top: 244px;
    width: 328px; height: 435px;
    border: 1px solid var(--rule);
    background: var(--paper);
    overflow: hidden;
  }
  .back-label__header {
    position: absolute; left: 0; top: 0; width: 100%; height: 106px;
    background: var(--charcoal);
  }
  .back-label__brand {
    position: absolute; top: 22px; width: 100%;
    text-align: center;
    font-size: 30px;
  }
  .back-label__title {
    position: absolute; top: 77px; width: 100%;
    text-align: center;
    font-family: "Raleway", sans-serif;
    font-size: 11px; letter-spacing: 2.2px;
    color: var(--paper);
  }
  .back-label__story {
    position: absolute; left: 0; top: 106px; width: 100%; height: 210px;
    background: var(--slate);
    color: var(--paper);
    padding: 10px 20px 0;
    text-align: center;
    font-size: 9.6px;
    line-height: 11.8px;
  }
  .back-label__story p + p { margin-top: 5px; }
  .back-label__address {
    margin-top: 8px;
    font-family: "Raleway", sans-serif;
    font-size: 8.5px; letter-spacing: 1.6px;
    line-height: 10.5px;
  }
  .back-label__barcode-area {
    position: absolute; left: 17px; top: 333px;
    width: 134px; height: 84px;
    border: 1px solid var(--rule);
    display: flex; align-items: center; justify-content: center;
    font-size: 9px; letter-spacing: .4px;
  }
  .back-label__abv {
    position: absolute; left: 161px; top: 330px;
    font-size: 13px;
  }
  .back-label__allergen {
    position: absolute; left: 161px; top: 348px;
    font-family: "Arimo", sans-serif;
    font-size: 9.5px;
  }
  .back-label__volume {
    position: absolute; left: 161px; top: 397px;
    font-size: 16px;
  }
  .back-label__std-label {
    position: absolute; left: 248px; top: 376px;
    transform: translate(-50%, -50%) rotate(-90deg);
    font-family: "Oswald", sans-serif;
    font-weight: 600;
    font-size: 11px;
    white-space: nowrap;
  }
  .back-label__std-glass { position: absolute; left: 266px; top: 330px; }
</style>
</head>
<body>
  <div class="caption caption--front-title">FRONT</div>
  <div class="caption caption--back-title">BACK</div>

  <section class="front-label" aria-label="Front label">
    <h1 class="front-label__title">LANTERNWATCH'S<br>RESERVE</h1>
    <div class="front-label__keys" role="img" aria-label="Engraved illustration of two antique keys on a ring"></div>
    <div class="front-label__vintage">2011</div>
    <div class="front-label__red-rule"></div>
    <div class="front-label__band"></div>
    <div class="front-label__crest-mark" aria-hidden="true"></div>
    <div class="front-label__brand brand-name">Harrowby Wines</div>
    <div class="front-label__region">MUDGEE, WINE OF AUSTRALIA</div>
  </section>

  <section class="back-label" aria-label="Back label">
    <div class="back-label__header">
      <div class="back-label__brand brand-name">Harrowby Wines</div>
      <h2 class="back-label__title">LANTERNWATCH'S RESERVE 2011</h2>
    </div>
    <div class="back-label__story">
      <p>Deep and intense purple hues with aromas of ripe blackberry fruits, spice and eucalypt with rich chocolate complemented by subtle oak overtones. A rich and full bodied wine exhibiting a soft yet generous palate with plum, forest fruits and mint chocolate notes.</p>
      <p>A fine grained tannin structure displaying integrated oak characters adds to the complexity of the wine. This wine was aged for 18 months in a blend of new French oak hogsheads and one year old American hogsheads, crafting a blend with great structure and length of flavour which will develop into a Mudgee classic” Lewis Farrant, Winemaker</p>
      <p class="back-label__address">HARROWBY WINES<br>TALLOWBEND RD, MUDGEE 2850<br>WWW.HARROWBYWINES.EXAMPLE.AU</p>
    </div>
    <div class="back-label__barcode-area">BARCODE AREA</div>
    <div class="back-label__abv">13.5% Alc/Vol.</div>
    <div class="back-label__allergen">Contains Sulphites</div>
    <div class="back-label__volume">750ml</div>
    <div class="back-label__std-label">Standard Drinks</div>
    <svg class="back-label__std-glass" width="46" height="90" viewBox="0 0 46 90" aria-label="8.0 standard drinks">
      <path d="M5 3 H41 Q45 38 23 52 Q1 38 5 3 Z" fill="none" stroke="#1a1a1a" stroke-width="3.2"/>
      <line x1="23" y1="52" x2="23" y2="84" stroke="#1a1a1a" stroke-width="3.2"/>
      <line x1="8" y1="85" x2="38" y2="85" stroke="#1a1a1a" stroke-width="3.2"/>
      <text x="23" y="30" text-anchor="middle" font-family="Arimo, sans-serif" font-size="15" fill="#1a1a1a">8.0</text>
    </svg>
  </section>

  <div class="caption caption--front-size">Size: 115mm (h) x 70mm (w)</div>
  <div class="caption caption--back-size">Size: 120mm (h) x 90mm (w)</div>
</body>
</html>
```